Website design for a Recruitment Agency in the Pacific Islands

Website for jobseekers to search for work, employers to list vacancies and also for workers to upload their resumes for possible job prospects.

The website will be called ' Korvani Staffing' and this needs to reflect the Pacific Islanders searching for jobs or working in the fields.
Must be connected to a database that collects details for workers which can be downloaded onto an excel spreadsheet for quick reviews offline
The website must also have an app for ios and android so this can be easily downloaded for individuals who want to do quick job searches without going onto the website.

The main objective of this website is to list job opportunities in all Pacific Island Countries or even overseas which Pacific Islanders can apply.

The theme of fishing means ' there is alot of fish in the sea ' = lots of workers in the Pacific Ocean.

Target Market(s)

Agriculture, Fisheries, constructions and mining

Industry/Entity Type

Agriculture, Constructions and Fisheries

Font styles to use
Other font styles liked:
• Muli

Colors
E54698
E96AAD
F1A4CE
F9D9EA
FCEFF6

Requirements
Must have
• Must have an App, adroid and ios
Nice to have
• - pictures of Pacific Islanders , pictures of Pacific Islanders at work in mines, in fisheries and in agricultures

```html
<!DOCTYPE html>
<html lang="en">
<head>
<meta charset="utf-8">
<title>Korvani Staffing — Recruitment across the Pacific</title>
<link rel="stylesheet" href="https://fonts.googleapis.com/css2?family=Barlow:wght@400;500;600;700&family=Roboto:ital,wght@0,400;0,500;1,400&display=swap">
<style>
:root{
  --pink:#e5007d;
  --pink-soft:#e96aad;
  --pink-pale:#f5cfe6;
  --pink-mist:#fceff6;
  --ink:#222;
  --text:#555;
  --muted:#888;
  --grey-bg:#f4f4f4;
  --dark:#1f1f21;
  --white:#fff;
}
*{margin:0;padding:0;box-sizing:border-box}
html,body{width:1200px;height:4215px;overflow:hidden}
body{position:relative;font-family:"Roboto",sans-serif;color:var(--text);background:var(--white)}
.abs{position:absolute}
.center{left:0;width:1200px;text-align:center}
h1,h2,h3{font-family:"Barlow",sans-serif;color:var(--ink);font-weight:600}
h2.section-title{position:absolute;left:0;width:1200px;text-align:center;font-size:40px;line-height:1;letter-spacing:.2px}
.lede{position:absolute;font-size:13px;line-height:26px;color:var(--text);text-align:center}
.btn{position:absolute;display:flex;align-items:center;justify-content:center;background:var(--pink);color:var(--white);font-family:"Barlow",sans-serif;font-weight:600;font-size:14px;text-transform:uppercase;text-decoration:none;box-shadow:0 6px 14px rgba(229,0,125,.25)}

/* header */
.topbar{top:0;left:0;width:1200px;height:54px;background:var(--pink-pale)}
.topbar-contact{top:18px;right:112px;display:flex;gap:22px;font-size:13px;color:var(--ink)}
.topbar-contact span{display:flex;align-items:center;gap:6px}
.brand-block{top:0;left:0;width:344px;height:124px}
.brand-name{top:48px;left:34px;font-family:"Barlow",sans-serif;font-weight:600;font-size:22px;color:var(--white);letter-spacing:.5px}
.main-nav{top:84px;left:386px;display:flex;gap:34px;font-size:14px;color:var(--ink)}
.main-nav a{color:inherit;text-decoration:none}
.main-nav a.active{color:var(--pink)}
.upload{top:69px;left:925px;width:164px;height:46px;box-shadow:none}

/* hero */
.hero{top:124px;left:0;width:1200px;height:642px;background:linear-gradient(180deg,#6b6f6c 0%,#8a8775 30%,#4f5a38 60%,#2c3b3a 100%)}
.hero-title{top:350px;font-size:66px;font-weight:700;color:var(--white);line-height:1}
.hero-copy{top:416px;left:285px;width:630px;color:var(--white);font-size:13px;line-height:26px}
.hero-cta{top:480px;left:489px;width:221px;height:57px}
.slider-dots{position:absolute;display:flex;gap:6px}
.slider-dots i{display:block;width:12px;height:12px;border-radius:50%;border:1.5px solid var(--white)}
.slider-dots i.on{border-color:var(--pink)}
.hero-dots{top:398px;left:1138px;flex-direction:column;gap:5px}

/* search */
.search-panel{top:674px;left:111px;width:978px;height:215px;background:var(--white);box-shadow:0 8px 26px rgba(0,0,0,.14)}
.search-panel h2{position:absolute;top:48px;left:0;width:978px;text-align:center;font-size:38px;line-height:1}
.field{position:absolute;top:113px;height:51px;border:1px solid #d8d8d8;font-size:12px;color:var(--text);padding:0 12px;display:flex;align-items:center}
.search-btn{top:113px;left:724px;width:218px;height:51px;font-size:13px;text-transform:none;font-family:"Roboto",sans-serif;font-weight:500}

/* industries */
.industry{top:889px;left:0;width:1200px;height:648px;background:linear-gradient(180deg,#fff 55%,#f6f2f8 100%)}
.industry-card{position:absolute;top:1133px;width:300px;height:319px;background:var(--white);border-radius:18px;box-shadow:0 4px 18px rgba(0,0,0,.12);text-align:center}
.tag{position:absolute;top:-8px;left:65px;width:170px;height:31px;background:var(--pink);color:var(--white);font-size:12px;font-weight:500;display:flex;align-items:center;justify-content:center;text-transform:uppercase}
.industry-card h3{position:absolute;top:63px;left:10px;width:280px;font-family:"Roboto",sans-serif;font-weight:500;font-size:12.5px;line-height:26px;text-transform:uppercase;color:var(--ink);white-space:nowrap}
.industry-card p{position:absolute;top:130px;left:20px;width:260px;font-size:11.5px;line-height:24px}
.apply{position:absolute;top:268px;left:0;width:300px;text-align:center;color:var(--pink);font-weight:500;font-size:13px;text-decoration:underline}

/* video */
.video{top:1537px;left:0;width:1200px;height:491px;background:linear-gradient(135deg,#5a4c3d 0%,#7b6a57 45%,#6d5b48 100%)}
.play{top:1683px;left:580px}
.video-title{top:1760px;font-size:40px;color:var(--white);font-weight:600;line-height:1}
.video-copy{top:1807px;left:165px;width:870px;color:var(--white)}

/* reviews */
.reviews{top:2028px;left:0;width:1200px;height:460px;background:linear-gradient(180deg,#fff 0%,#fff 70%,#f7f1f6 100%)}
.quote-mark{top:2178px;left:575px}
.review-text{top:2244px;left:110px;width:980px;font-style:italic}
.reviewer{top:2354px;font-size:14px;color:var(--ink)}
.reviewer-role{top:2378px;font-size:13px;color:var(--muted)}
.slider-dots.pink i{border-color:var(--ink);width:11px;height:11px}
.slider-dots.pink i.on{border-color:var(--pink)}

/* news */
.news{top:2488px;left:0;width:1200px;height:717px;background:var(--grey-bg)}
.news-card{position:absolute;top:2685px;width:317px;height:412px;background:var(--white);box-shadow:0 2px 10px rgba(0,0,0,.1)}
.news-card .photo{width:317px;height:187px}
.news-card h3{position:absolute;top:202px;left:15px;width:290px;font-family:"Roboto",sans-serif;font-weight:500;font-size:14px;line-height:27px;color:var(--ink)}
.news-card p{position:absolute;top:262px;left:15px;width:290px;font-size:12px;line-height:23px;color:var(--muted)}
.news-card .meta{position:absolute;top:348px;left:17px;font-family:"Barlow",sans-serif;font-size:12px;color:var(--ink)}

/* about */
.about-title{top:3295px;left:112px;font-size:40px;line-height:1}
.about-copy{top:3346px;left:111px;width:460px;font-size:12.5px;line-height:25.5px;text-align:left}
.about-copy p+p{margin-top:25px}
.about-photo{top:3282px;left:634px;width:453px;height:439px;background:linear-gradient(160deg,#c9a26b 0%,#a5793f 45%,#5e4a2a 100%);box-shadow:0 6px 18px rgba(0,0,0,.2)}
.read-more{top:3644px;left:111px;width:197px;height:57px}

/* footer */
.footer{top:3793px;left:0;width:1200px;height:422px;background:linear-gradient(180deg,#29292b 0%,#1c1c1e 100%)}
.newsletter-title{top:3853px;font-size:30px;color:var(--white);font-weight:600;line-height:1}
.email-field{top:3911px;left:295px;width:407px;height:51px;background:var(--white);font-size:13px;color:var(--ink);padding-left:16px;display:flex;align-items:center}
.subscribe{top:3911px;left:702px;width:203px;height:51px;font-size:20px;border:2px solid var(--white);box-shadow:none}
.socials{top:3984px;left:474px;display:flex;gap:17px}
.socials span{width:36px;height:36px;border-radius:50%;border:2px solid var(--white);display:flex;align-items:center;justify-content:center}
.socials svg{width:16px;height:16px;fill:none;stroke:var(--white);stroke-width:2;stroke-linecap:round;stroke-linejoin:round}
.footer-rule{top:4057px;left:111px;width:978px;height:1px;background:#6a6a6a}
.footer-nav{top:4103px;left:0;width:1200px;display:flex;justify-content:center;gap:36px;font-size:15px;color:var(--white);text-transform:uppercase}
.copyright{top:4150px;font-size:14px;color:var(--white)}
</style>
</head>
<body>

<!-- Header -->
<div class="abs topbar"></div>
<div class="abs topbar-contact">
  <span><svg width="12" height="12" viewBox="0 0 24 24" fill="#e5007d"><path d="M6.6 10.8a15 15 0 0 0 6.6 6.6l2.2-2.2c.3-.3.7-.4 1-.2 1.1.4 2.3.6 3.6.6.6 0 1 .4 1 1V20c0 .6-.4 1-1 1C10.6 21 3 13.4 3 4c0-.6.4-1 1-1h3.5c.6 0 1 .4 1 1 0 1.3.2 2.5.6 3.6.1.3 0 .7-.2 1z"/></svg>CALL NOW - +1 555 010 0199</span>
  <span><svg width="14" height="12" viewBox="0 0 24 20" fill="#e5007d"><path d="M2 0h20a2 2 0 0 1 2 2v16a2 2 0 0 1-2 2H2a2 2 0 0 1-2-2V2a2 2 0 0 1 2-2zm10 11L2 4v2l10 7 10-7V4z"/></svg>EMAIL - korvani-staffing.example</span>
</div>
<svg class="abs brand-block" viewBox="0 0 344 124"><polygon points="0,0 229,0 344,124 0,124" fill="var(--pink)"/></svg>
<div class="abs brand-name">Korvani Staffing</div>
<nav class="abs main-nav">
  <a class="active" href="#">HOME</a><a href="#">ABOUT US</a><a href="#">SERVICES</a><a href="#">JOBS</a><a href="#">REVIEWS</a><a href="#">CONTACT</a>
</nav>
<a class="btn upload" href="#">UPLOAD RESUME</a>

<!-- Hero -->
<section class="abs hero" role="img" aria-label="Photo of green island hills and a bay at dusk"></section>
<h1 class="abs center hero-title">KORVANI.</h1>
<p class="lede hero-copy">Lorem ipsum dolor sit amet, consectetur adipiscing elit, sed do eiusmod tempor incididunt ut labore et<br>dolore magna aliqua. Ut enim ad minim veniam, quis nostrud exercitation ullamco laboris</p>
<a class="btn hero-cta" href="#">GET STARTED</a>
<div class="slider-dots hero-dots"><i class="on"></i><i></i><i></i><i></i><i></i><i></i></div>

<!-- Industries background -->
<div class="abs industry"></div>

<!-- Search -->
<section class="abs search-panel">
  <h2>SEARCH FOR PROFESSIONALS</h2>
  <div class="field" style="left:35px;width:219px">Job Category</div>
  <div class="field" style="left:265px;width:218px">Location</div>
  <div class="field" style="left:495px;width:217px">Job Type</div>
  <a class="btn search-btn" href="#">Search</a>
</section>

<!-- Job industry -->
<h2 class="section-title" style="top:975px">OUR JOB INDUSTRY</h2>
<p class="lede" style="top:1035px;left:240px;width:720px">Lorem ipsum dolor sit amet, consectetur adipiscing elit, sed do eiusmod tempor incididunt ut labore et dolore magna<br>aliqua. Ut enim ad minim veniam, quis nostrud exercitation</p>

<article class="industry-card" style="left:111px">
  <span class="tag">Agriculture</span>
  <h3>Lorem ipsum dolor sit amet,<br>adipiscing elit, sed do eiusmod tempor</h3>
  <p>Lorem ipsum dolor sit amet, adipiscing elit, sed do eiusmod tempor incididunt ut labore et dolore magna aliqua. Ut enim ad minim veniam, quis nostrud exercitation ullamco laboris nisi ut aliquip ex ea commodo consequat.</p>
  <a class="apply" href="#">APPLY NOW</a>
</article>
<article class="industry-card" style="left:450px">
  <span class="tag">Constructions</span>
  <h3>Lorem ipsum dolor sit amet,<br>adipiscing elit, sed do eiusmod tempor</h3>
  <p>Lorem ipsum dolor sit amet, adipiscing elit, sed do eiusmod tempor incididunt ut labore et dolore magna aliqua. Ut enim ad minim veniam, quis nostrud exercitation ullamco laboris nisi ut aliquip ex ea commodo consequat.</p>
  <a class="apply" href="#">APPLY NOW</a>
</article>
<article class="industry-card" style="left:789px">
  <span class="tag">Fisheries</span>
  <h3>Lorem ipsum dolor sit amet,<br>adipiscing elit, sed do eiusmod tempor</h3>
  <p>Lorem ipsum dolor sit amet, adipiscing elit, sed do eiusmod tempor incididunt ut labore et dolore magna aliqua. Ut enim ad minim veniam, quis nostrud exercitation ullamco laboris nisi ut aliquip ex ea commodo consequat.</p>
  <a class="apply" href="#">APPLY NOW</a>
</article>

<!-- Video -->
<section class="abs video" role="img" aria-label="Photo of construction workers in hard hats reviewing plans at a wooden table"></section>
<svg class="abs play" width="40" height="40" viewBox="0 0 40 40"><circle cx="20" cy="20" r="18" fill="none" stroke="#fff" stroke-width="2.5"/><polygon points="16,12 28,20 16,28" fill="#fff"/></svg>
<h2 class="abs center video-title">WATCH OUR VIDEO</h2>
<p class="lede video-copy">Lorem ipsum dolor sit amet, consectetur adipiscing elit, sed do eiusmod tempor incididunt ut labore et dolore magna aliqua. Ut enim ad minim<br>veniam, quis nostrud exercitation ullamco laboris nisi ut aliquip ex ea commodo consequat. Duis aute irure dolor in reprehenderit<br>in voluptate velit esse cillum dolore</p>

<!-- Reviews -->
<div class="abs reviews"></div>
<h2 class="section-title" style="top:2092px">CUSTOMER REVIEWS</h2>
<svg class="abs quote-mark" width="50" height="42" viewBox="0 0 50 42" fill="var(--pink)"><path d="M2 42V24C2 10 8 3 20 0l2 5c-7 2-10 7-10 13h9v24zM28 42V24C28 10 34 3 46 0l2 5c-7 2-10 7-10 13h9v24z"/></svg>
<p class="lede review-text">Lorem ipsum dolor sit amet, consectetur adipiscing elit, sed do eiusmod tempor incididunt ut labore et dolore magna aliqua. Ut enim ad minim veniam, quis nostrud<br>exercitation ullamco laboris nisi ut aliquip ex ea commodo consequat. Duis aute irure dolor in reprehenderit in voluptate velit esse cillum dolore eu fugiat nulla<br>pariatur. Excepteur sint occaecat cupidatat non proident, sunt in culpa qui officia deserunt mollit anim id est laborum</p>
<div class="abs center reviewer">Leilani Tuvalu</div>
<div class="abs center reviewer-role">Lorem ipsum</div>
<div class="slider-dots pink" style="top:2418px;left:556px;gap:4px"><i class="on"></i><i></i><i></i><i></i><i></i><i></i></div>

<!-- News -->
<section class="abs news"></section>
<h2 class="section-title" style="top:2553px">NEWS &amp; ARTICLES</h2>
<p class="lede" style="top:2601px;left:310px;width:580px">Lorem ipsum dolor sit amet, consectetur adipiscing elit, sed do eiusmod tempor incididunt ut labore et<br>dolore magna aliqua. Ut enim ad minim veniam, quis nostrud</p>

<article class="news-card" style="left:113px">
  <div class="photo" role="img" aria-label="Photo of a fisher holding a net with yellow floats by the sea" style="background:linear-gradient(135deg,#6f8fb3 0%,#c9a958 55%,#8a4a3a 100%)"></div>
  <h3>Lorem ipsum dolor sit amet, consectetur adipiscing elit</h3>
  <p>Lorem ipsum dolor sit amet, adipiscing elit, sed do eiusmod tempor incididunt ut dolore magna aliqua. Ut enim ad minim veniam,</p>
  <div class="meta">25 Aug 2022 &nbsp;|&nbsp; 0 Comment &nbsp;|&nbsp; Admin</div>
</article>
<article class="news-card" style="left:444px">
  <div class="photo" role="img" aria-label="Photo of a hand planting seeds in dark soil" style="background:linear-gradient(135deg,#4a3a30 0%,#2f251f 60%,#5a4538 100%)"></div>
  <h3>Lorem ipsum dolor sit amet, consectetur adipiscing elit</h3>
  <p>Lorem ipsum dolor sit amet, adipiscing elit, sed do eiusmod tempor incididunt ut dolore magna aliqua. Ut enim ad minim veniam,</p>
  <div class="meta">25 Aug 2022 &nbsp;|&nbsp; 0 Comment &nbsp;|&nbsp; Admin</div>
</article>
<article class="news-card" style="left:773px">
  <div class="photo" role="img" aria-label="Photo of fishermen sorting a catch on the deck of a boat" style="background:linear-gradient(135deg,#3f6a96 0%,#8e9aa8 50%,#2f5d8a 100%)"></div>
  <h3>Lorem ipsum dolor sit amet, consectetur adipiscing elit</h3>
  <p>Lorem ipsum dolor sit amet, adipiscing elit, sed do eiusmod tempor incididunt ut dolore magna aliqua. Ut enim ad minim veniam,</p>
  <div class="meta">25 Aug 2022 &nbsp;|&nbsp; 0 Comment &nbsp;|&nbsp; Admin</div>
</article>
<div class="slider-dots pink" style="top:3132px;left:566px;gap:3px"><i></i><i></i><i class="on"></i><i></i><i></i></div>

<!-- About -->
<h2 class="abs about-title">ABOUT US</h2>
<div class="lede about-copy">
  <p>Lorem ipsum dolor sit amet, consectetur adipiscing elit, sed do eiusmod tempor incididunt ut labore et dolore magna aliqua. Ut enim ad veniam, quis nostrud exercitation ullamco laboris nisi ut aliquip ex ea consequat. aute irure dolor in reprehenderit in voluptate velit esse cillum dolore eu fugiat nulla pariatur. Excepteur sint occaecat cupidatat non culpa qui officia deserunt mollit anim id est laborum.</p>
  <p>Lorem ipsum dolor sit amet, consectetur adipiscing elit, sed do eiusmod tempor incididunt ut labore et dolore magna aliqua. Ut enim ad veniam, quis nostrud exercitation ullamco laboris nisi ut aliquip ex ea consequat. aute irure dolor in reprehenderit in voluptate</p>
</div>
<div class="abs about-photo" role="img" aria-label="Photo of a farmer holding a tablet over a golden grain field"></div>
<a class="btn read-more" href="#">READ MORE</a>

<!-- Footer -->
<footer class="abs footer"></footer>
<h2 class="abs center newsletter-title">SUBSCRIBE TO OUR NEWSLETTER</h2>
<div class="abs email-field">Email</div>
<a class="btn subscribe" href="#">SUBSCRIBE</a>
<div class="abs socials" aria-label="Contact and sharing links">
  <span aria-label="Website"><svg viewBox="0 0 24 24"><circle cx="12" cy="12" r="9"/><path d="M3 12h18M12 3c3 3 3 15 0 18M12 3c-3 3-3 15 0 18"/></svg></span>
  <span aria-label="Email"><svg viewBox="0 0 24 24"><rect x="3" y="6" width="18" height="12" rx="1"/><path d="M3 7l9 6 9-6"/></svg></span>
  <span aria-label="Chat"><svg viewBox="0 0 24 24"><path d="M4 5h16v11H9l-5 4z"/></svg></span>
  <span aria-label="Share"><svg viewBox="0 0 24 24"><circle cx="6" cy="12" r="2.5"/><circle cx="18" cy="6" r="2.5"/><circle cx="18" cy="18" r="2.5"/><path d="M8.2 11l7.6-4M8.2 13l7.6 4"/></svg></span>
  <span aria-label="Phone"><svg viewBox="0 0 24 24"><path d="M6.6 10.8a15 15 0 0 0 6.6 6.6l2.2-2.2 4.6 1.4V20C10.6 21 3 13.4 4 4h3.5l1.4 4.6z"/></svg></span>
</div>
<div class="abs footer-rule"></div>
<nav class="abs footer-nav"><span>Home</span><span>About Us</span><span>Services</span><span>Jobs</span><span>Reviews</span><span>Contact</span></nav>
<div class="abs center copyright">Copyrights © 2022 All Rights Reserved</div>

</body>
</html>
```